THE PRACTICE NAME "The Renal Crest MD" FOR A NEW MEDICAL PRACTICE STARTUP

THIS IS A BUSINESS CARD REQUEST FOR A KIDNEY DOCTOR's(NEPHROLOGIST) PRACTICE, THIS PRACTICE WILL BE IN EL PASO,TEXAS USA.OPEN TO INNOVATIVE IDEAS!

THE RENAL CREST MD ( NAME OF PRACTICE)

VIKRANT L. MOTHRE, MD FNKF FASN ( NAME OF PHYSICIAN WITH DEGREES)
BOARD CERTIFIED INTERNAL MEDICINE
BOARD CERTIFIED NEPHROLOGY
HYPERTENSION SPECIALIST

OFFICE ADDRESS, PHONE, FAX AND EMAIL PENDING

Guarding Health. Building Futures.(MOTTO) THE LOGO SHOILD REFLECT THIS MESSAGE. WE NEED A LOGO DESIGN WITH 2 KIDNEYS OR CAN BE ONE KIDNEY ALSO.

Target Market(s)

PATIENTS WITH KIDNEY DISEASE, HYPERTENSION, ENGLISH AND SPANISH SPEAKING POPULATION AND PATIENTS ON DIALYSIS

Industry/Entity Type

Health Care

Contact Information for Business Card

HYPERTENSION SPECIALIST

WEBSITE URL PENDING

Font styles to use
Serif
Sans Serif
Script

Colors
fbed38
ffc214
fbf289
fbee3e
5c5c5c
333333
1b1b1b
757575
d3d3d3

Requirements
Must have
• A KIDNEY LOGO
• NAME OF THE PRACTICE
Nice to have
• IF THE CARD CAN BE IN THE SHAPE OF A KIDNEY

```html
<!DOCTYPE html>
<html lang="en">
<head>
<meta charset="utf-8">
<title>The Renal Crest MD – Business Card</title>
<link rel="stylesheet" href="https://fonts.googleapis.com/css2?family=Source+Sans+3:wght@400;600&display=swap">
<style>
  :root {
    --card-white: #ffffff;
    --ink: #1b1b1b;
    --panel-dark: #111414;
    --mist: #d3d3d3;
    --sun: #ffc214;
    --trim: #5ecbf0;
  }
  html, body {
    margin: 0;
    padding: 0;
    width: 1200px;
    height: 746px;
    overflow: hidden;
    background: var(--card-white);
  }
  .card {
    position: relative;
    width: 1200px;
    height: 746px;
    background: var(--card-white);
    font-family: "Source Sans 3", "Myriad Pro", sans-serif;
    color: var(--ink);
    overflow: hidden;
  }
  .trim-line {
    position: absolute;
    inset: 1px;
    border: 2px solid var(--trim);
    pointer-events: none;
    z-index: 3;
  }
  .physician {
    position: absolute;
    left: 126px;
    top: 86px;
  }
  .physician-name {
    margin: 0;
    font-size: 52px;
    font-weight: 600;
    line-height: 52px;
  }
  .physician-degrees {
    margin: 7px 0 0;
    font-size: 38px;
    font-weight: 400;
    line-height: 38px;
  }
  .credentials {
    list-style: none;
    margin: 28px 0 0;
    padding: 0;
    font-size: 36px;
    line-height: 45.5px;
  }
  .contact {
    position: absolute;
    left: 126px;
    top: 458px;
    font-style: normal;
    font-size: 36px;
    line-height: 45.5px;
  }
  .contact-company {
    display: block;
    font-size: 42px;
    font-weight: 600;
    line-height: 42px;
    margin-bottom: 4px;
  }
  .contact-line { display: block; }
  .brand-panel {
    position: absolute;
    left: 782px;
    top: 0;
    width: 358px;
    height: 746px;
    background: var(--panel-dark);
  }
  .practice-mark {
    position: absolute;
    left: 0;
    right: 0;
    top: 96px;
    text-align: center;
  }
  .practice-dot {
    display: block;
    width: 56px;
    height: 56px;
    margin: 0 auto 20px;
    border-radius: 50%;
    background: var(--sun);
  }
  .practice-name {
    font-weight: 600;
    font-size: 34px;
    line-height: 40px;
    color: var(--mist);
  }
  .motto {
    position: absolute;
    left: 0;
    right: 0;
    top: 600px;
    margin: 0;
    text-align: center;
    font-size: 26px;
    font-weight: 400;
    line-height: 32px;
    color: var(--mist);
  }
</style>
</head>
<body>
  <div class="card">
    <section class="physician">
      <h1 class="physician-name">Vikrant L. Mothre</h1>
      <p class="physician-degrees">MD FNKF FASN</p>
      <ul class="credentials">
        <li>Board Certifield Internel Medicine</li>
        <li>Board Certifield Nephrology</li>
        <li>Hypertension Specialist</li>
      </ul>
    </section>

    <address class="contact">
      <span class="contact-company">Company Name</span>
      <span class="contact-line">#Address</span>
      <span class="contact-line">Tel:</span>
      <span class="contact-line">Fax:</span>
      <span class="contact-line">Email:</span>
    </address>

    <aside class="brand-panel">
      <div class="practice-mark">
        <span class="practice-dot"></span>
        <div class="practice-name">The Renal Crest MD</div>
      </div>
      <p class="motto">Guarding Health.<br>Building Futures.</p>
    </aside>

    <div class="trim-line"></div>
  </div>
</body>
</html>
```